Pemberton Dialworks Business Card Design

Double Sided Business Card Design for a Locksmith company specializing in Safecracking, safe & vault service.

```html
<!DOCTYPE html>
<html lang="en">
<head>
<meta charset="utf-8">
<title>Pemberton Dialworks Business Card</title>
<link href="https://fonts.googleapis.com/css2?family=Poppins:wght@300;400;700;800&display=swap" rel="stylesheet">
<style>
  :root {
    --stage: #7d7c7a;
    --charcoal: #2b2828;
    --paper: #fbfbfa;
    --mist: #e3e3e2;
    --green: #21903f;
    --ink: #1f1f1f;
    --soft-ink: #4a4a4a;
  }
  * { box-sizing: border-box; margin: 0; padding: 0; }
  html, body { width: 1200px; height: 1200px; overflow: hidden; }
  body {
    background: var(--stage);
    font-family: "Poppins", sans-serif;
    display: flex; flex-direction: column; align-items: center; justify-content: center;
    gap: 60px;
  }
  .card {
    position: relative; width: 840px; height: 480px;
    border-radius: 34px; overflow: hidden;
    box-shadow: 0 18px 40px rgba(0,0,0,0.28);
  }

  /* Back side: contact details */
  .card-back { background: var(--paper); }
  .back-dark { position: absolute; left: 0; top: 0; width: 370px; height: 100%; background: var(--charcoal); }
  .back-accent { position: absolute; left: 0; top: 92px; width: 26px; height: 96px; background: var(--green); }
  .back-strip { position: absolute; left: 370px; top: 0; width: 44px; height: 100%; background: var(--mist); }
  .brand-block { position: absolute; left: 70px; top: 170px; display: flex; align-items: center; gap: 14px; }
  .brand-dot { width: 46px; height: 46px; border-radius: 50%; background: var(--green); flex: none; }
  .brand-name { color: #fff; font-weight: 800; font-size: 24px; line-height: 1.1; letter-spacing: 0.5px; text-transform: uppercase; }

  .icon-tile {
    position: absolute; left: 334px; width: 72px; height: 64px;
    background: var(--green); display: flex; align-items: center; justify-content: center;
  }
  .icon-tile svg { width: 30px; height: 30px; fill: none; stroke: #fff; stroke-width: 2; }
  .icon-tile svg .solid { fill: #fff; stroke: none; }

  .person-name { position: absolute; left: 440px; top: 118px; font-size: 34px; color: var(--ink); font-weight: 300; letter-spacing: 0.5px; }
  .person-name strong { font-weight: 700; }
  .person-role { position: absolute; left: 440px; top: 160px; font-size: 19px; color: var(--soft-ink); font-weight: 300; }
  .contact-row { position: absolute; left: 440px; font-size: 15px; line-height: 1.35; color: var(--soft-ink); font-weight: 300; }
  .rule { position: absolute; left: 406px; right: 0; height: 2px; background: var(--green); }

  /* Front side: brand */
  .card-front { background: var(--charcoal); }
  .front-brand { position: absolute; left: 0; right: 0; top: 120px; display: flex; justify-content: center; align-items: center; gap: 20px; }
  .front-brand .brand-dot { width: 78px; height: 78px; }
  .front-brand .brand-name { font-size: 40px; }
  .front-rule { position: absolute; left: 0; right: 0; top: 332px; height: 8px; background: var(--green); }
  .front-band { position: absolute; left: 0; right: 0; top: 340px; bottom: 0; background: var(--paper); display: flex; align-items: center; justify-content: center; }
  .web-address { font-size: 26px; font-weight: 300; color: var(--ink); letter-spacing: 0.5px; }
</style>
</head>
<body>

  <section class="card card-back" aria-label="Card back">
    <div class="back-dark"></div>
    <div class="back-accent"></div>
    <div class="back-strip"></div>
    <div class="brand-block">
      <div class="brand-dot"></div>
      <div class="brand-name">Pemberton<br>Dialworks</div>
    </div>

    <div class="icon-tile" style="top:98px">
      <svg viewBox="0 0 30 30"><circle class="solid" cx="15" cy="10" r="6"/><path class="solid" d="M4 27c0-7 5-10 11-10s11 3 11 10z"/></svg>
    </div>
    <div class="icon-tile" style="top:196px">
      <svg viewBox="0 0 30 30"><rect x="9" y="3" width="12" height="24" rx="2"/><line x1="13" y1="23" x2="17" y2="23"/></svg>
    </div>
    <div class="icon-tile" style="top:274px">
      <svg viewBox="0 0 30 30"><rect x="4" y="8" width="22" height="15"/><path d="M4 8l11 9 11-9M4 23l8-7M26 23l-8-7"/></svg>
    </div>
    <div class="icon-tile" style="top:352px">
      <svg viewBox="0 0 30 30"><path d="M15 27s-8-9-8-15a8 8 0 0 1 16 0c0 6-8 15-8 15z"/><circle cx="15" cy="12" r="3"/></svg>
    </div>

    <div class="person-name"><strong>CORIN</strong> ASHBY</div>
    <div class="person-role">Graphic Designer</div>
    <div class="contact-row" style="top:202px">555 . 210 48193726<br>555 . 210 48193726</div>
    <div class="rule" style="top:262px"></div>
    <div class="contact-row" style="top:280px">hello@corinashby.net<br>desk@corinashby.net</div>
    <div class="rule" style="top:340px"></div>
    <div class="contact-row" style="top:358px">Harlow Street, Suite#4<br>Eastgate Lane, NY -038</div>
    <div class="rule" style="top:418px"></div>
  </section>

  <section class="card card-front" aria-label="Card front">
    <div class="front-brand">
      <div class="brand-dot"></div>
      <div class="brand-name">Pemberton<br>Dialworks</div>
    </div>
    <div class="front-rule"></div>
    <div class="front-band"><span class="web-address">www.dialworksstudio.com</span></div>
  </section>

</body>
</html>
```